Book Cover for Willow Kindred Notes from the Meadow

We have written a book that brings together Notes from the Meadow from a variety of women's voices.
We developed a draft book cover that we like using Canva (attached below). We'd love a book cover that is similar to this image, but looks more professional.
Following are the themes we’d like to depict in the book cover, and in parentheses, how they are represented in the current cover:
1. Divinely feminine (overall cover)
2. Currents of enlightenment (the swirls of light carrying the butterfly)
3. Diversity (a myriad of colors)
4. The solo journey into the unknown (the single butterfly’s flight)
5. Buoyancy and joy (again, the dancing colors and floating butterfly)
6. Boldly feminine (the blue butterfly, set against brush strokes of light)
7. Homage to a dear friend (she loved blue butterflies, the cosmos - this butterfly has hints of the cosmos in her wings, and painting - this background has brush strokes of light).
Book Title, Subtitle, and Editor:
Willow Kindred
Notes from the Meadow
Edited by Mirela Tove
Thank you very much for considering this project!
People who are interested in Women and Spirituality

```html
<!DOCTYPE html>
<html lang="en">
<head>
<meta charset="UTF-8">
<title>Willow Kindred — Notes from the Meadow</title>
<link href="https://fonts.googleapis.com/css2?family=Montserrat:wght@600;700&family=Playball&display=swap" rel="stylesheet">
<style>
  :root {
    --stage: #c9c9c9;
    --pink: #f2bfd0;
    --rose: #eeb3c6;
    --blush: #f8e4ec;
    --lavender: #d6c8ea;
    --lilac: #c3b3e0;
    --periwinkle: #a9b5e6;
    --mist: #e4e2f3;
    --deep-blue: #1d5ba8;
    --teal: #13a9c1;
    --wing-light: #2ec0d6;
    --wing-mid: #1d95c9;
    --wing-deep: #1f58b0;
  }
  * { margin: 0; padding: 0; box-sizing: border-box; }
  html, body {
    width: 1200px;
    height: 848px;
    overflow: hidden;
    background: var(--stage);
  }
  .stage {
    position: relative;
    width: 1200px;
    height: 848px;
  }
  .cover {
    position: absolute;
    left: 340px;
    top: 34px;
    width: 520px;
    height: 780px;
    overflow: hidden;
    background:
      radial-gradient(ellipse 45% 22% at 62% 10%, var(--rose) 0%, transparent 70%),
      radial-gradient(ellipse 40% 30% at 88% 30%, var(--pink) 0%, transparent 70%),
      radial-gradient(ellipse 35% 18% at 18% 22%, var(--pink) 0%, transparent 75%),
      radial-gradient(ellipse 50% 25% at 75% 48%, var(--blush) 0%, transparent 70%),
      radial-gradient(ellipse 40% 30% at 15% 55%, var(--lilac) 0%, transparent 70%),
      radial-gradient(ellipse 45% 25% at 85% 70%, var(--mist) 0%, transparent 70%),
      radial-gradient(ellipse 50% 30% at 10% 90%, var(--periwinkle) 0%, transparent 75%),
      radial-gradient(ellipse 45% 20% at 60% 95%, var(--mist) 0%, transparent 70%),
      linear-gradient(180deg, var(--blush) 0%, var(--pink) 25%, var(--lavender) 55%, var(--periwinkle) 100%);
  }
  .cover__title {
    position: absolute;
    top: 78px;
    left: 0;
    width: 100%;
    text-align: center;
    font-family: "Montserrat", sans-serif;
    font-weight: 700;
    font-size: 76px;
    line-height: 0.95;
    text-transform: uppercase;
    background: linear-gradient(90deg, var(--deep-blue) 0%, var(--teal) 55%, var(--deep-blue) 100%);
    -webkit-background-clip: text;
    background-clip: text;
    color: transparent;
  }
  .cover__subtitle {
    position: absolute;
    top: 236px;
    left: 0;
    width: 100%;
    text-align: center;
    font-family: "Playball", cursive;
    font-size: 42px;
    transform: rotate(-7deg);
    background: linear-gradient(90deg, var(--deep-blue) 0%, var(--teal) 55%, var(--deep-blue) 100%);
    -webkit-background-clip: text;
    background-clip: text;
    color: transparent;
  }
  .cover__art {
    position: absolute;
    left: 48px;
    top: 300px;
    width: 420px;
    height: 360px;
    background:
      radial-gradient(ellipse 30% 40% at 72% 30%, var(--wing-light) 0%, transparent 75%),
      radial-gradient(ellipse 35% 30% at 38% 62%, var(--wing-light) 0%, transparent 75%),
      radial-gradient(ellipse 50% 50% at 55% 55%, var(--wing-mid) 0%, var(--wing-deep) 55%, transparent 72%);
  }
  .cover__editor {
    position: absolute;
    right: 62px;
    top: 682px;
    font-family: "Montserrat", sans-serif;
    font-weight: 700;
    font-size: 17px;
    color: var(--teal);
  }
</style>
</head>
<body>
  <main class="stage">
    <section class="cover">
      <h1 class="cover__title">Willow<br>Kindred</h1>
      <p class="cover__subtitle">Notes from the Meadow</p>
      <div class="cover__art" role="img" aria-label="Iridescent blue butterfly in flight, wings spread, with starry glints on the wing tips"></div>
      <p class="cover__editor">Edited by Mirela Tove</p>
    </section>
  </main>
</body>
</html>
```